RTM Global (Rooted Tillage and Meadowcraft) is a company positioning itself as a global leader in regenerative and sustainable agriculture and irrigation technologies and solutions, with a focus on soil health. Please read the attached information (which can be used in the website).
We're looking for a modern website which also compliments the agricultural sector and the natural resources we work with. We want the website to be fairly concise and to the point without elaborating too much. We would rather attract the clients to engage with us rather than drawing their own conclusions from the website.

```html
<!DOCTYPE html>
<html lang="en">
<head>
<meta charset="utf-8">
<title>RTM Global — Rooted Tillage and Meadowcraft</title>
<link rel="stylesheet" href="https://fonts.googleapis.com/css2?family=Roboto:wght@300;400;500;700&family=Arimo:wght@400;700&display=swap">
<style>
:root{
  --blue:#3f5f8e;
  --blue-deep:#2f4f80;
  --sage:#8a9878;
  --beige:#c3b398;
  --paper:#ece8df;
  --ghost:#ebe7df;
  --ink:#222;
  --muted:#444;
  --dark:#2a2824;
  --white:#fff;
}
*{margin:0;padding:0;box-sizing:border-box}
html,body{width:1200px;height:3277px;overflow:hidden;background:var(--white)}
body{position:relative;font-family:"Arimo",Arial,sans-serif;color:var(--ink)}
.abs{position:absolute}
.heading{font-family:"Roboto",Arial,sans-serif;font-weight:300}
.stripe{position:absolute;left:0;width:1200px;height:4px;display:flex;z-index:5}
.stripe span{flex:1}
.stripe span:nth-child(1){background:#6d6a62}
.stripe span:nth-child(2){background:var(--blue)}
.stripe span:nth-child(3){background:var(--sage)}
.stripe span:nth-child(4){background:var(--beige)}

/* buttons */
.btn{position:absolute;display:flex;align-items:center;justify-content:space-between;background:var(--blue);color:var(--white);border-radius:22px;font:700 12px "Arimo",Arial,sans-serif;letter-spacing:.3px;padding:0 5px 0 18px;text-transform:uppercase}
.btn .dot{width:28px;height:28px;border-radius:50%;background:var(--white);display:flex;align-items:center;justify-content:center}
.btn .dot svg{width:14px;height:14px}

/* hero */
.hero{top:0;left:0;width:1200px;height:672px}
.hero-photo{position:absolute;inset:0;background:
  radial-gradient(circle at 690px 360px,#c7832d 0,#6a7c57 70px,#3b5a72 115px,rgba(40,30,24,0) 160px),
  radial-gradient(ellipse at 690px 170px,#8fc23a 0,rgba(60,80,30,.0) 110px),
  radial-gradient(ellipse at 1110px 600px,#3a3d44 0,rgba(0,0,0,0) 120px),
  linear-gradient(180deg,#2a2522 0,#2e2824 55%,#5a3a22 80%,#6b4528 100%)}
.logo{position:absolute;display:flex;align-items:center;gap:9px;color:var(--white);font:700 30px "Roboto",Arial,sans-serif;letter-spacing:-.5px}
.logo .mark{width:14px;height:14px;border-radius:50%;background:var(--white)}
.nav{position:absolute;top:52px;left:0;width:1200px;font:400 12.5px "Arimo",Arial,sans-serif;color:var(--white)}
.nav a{position:absolute;transform:translateX(-50%);white-space:nowrap;text-decoration:none;color:inherit}
.nav a.active{color:#c9b79a}
.btn-contact{top:44px;left:963px;width:112px;height:34px;background:var(--sage);font-weight:400;text-transform:none;font-size:12px;padding-left:16px;border-radius:17px}
.btn-contact .dot{width:24px;height:24px}
.hero-rule{position:absolute;left:121px;top:193px;width:2px;height:84px;background:var(--white)}
.hero-title{position:absolute;left:136px;top:185px;color:var(--white);font:300 46px/53px "Roboto",Arial,sans-serif}
.hero-title b{font-weight:700}
.hero-list{position:absolute;left:122px;top:407px;list-style:none;color:var(--white);font:400 14.5px/24.5px "Roboto",Arial,sans-serif}
.hero-list li{display:flex;align-items:center;gap:9px}
.hero-list li::before{content:"";width:8px;height:8px;border-radius:50%;background:#d9d5cc}

/* framed photo */
.frame-back{position:absolute;background:var(--paper)}
.ring{position:absolute;border-radius:50%;background:var(--sage)}
.disc{position:absolute;border-radius:50%;border:5px solid var(--white);box-shadow:0 0 0 3px var(--sage)}
.ghost-word{position:absolute;font:700 66px "Roboto",Arial,sans-serif;color:var(--ghost);white-space:nowrap;transform-origin:0 0}
.eyebrow{position:absolute;font:700 12.5px "Arimo",Arial,sans-serif;color:var(--blue);display:flex;align-items:center;gap:8px}
.eyebrow .line{width:55px;height:1px;background:var(--blue)}
.eyebrow.center{left:0;width:1200px;justify-content:center}
.title{position:absolute;font:300 34px "Roboto",Arial,sans-serif;color:var(--ink)}
.para{position:absolute;font:400 10.5px/17px "Arimo",Arial,sans-serif;color:var(--muted)}

/* services */
.card{position:absolute;top:1334px;width:225px;height:305px;background:var(--beige);border-radius:10px;padding:6px;color:var(--white)}
.card .shot{height:157px;border-radius:4px}
.card h3{font:700 14.5px/17px "Arimo",Arial,sans-serif;margin:14px 6px 6px}
.card p{font:400 10px/14px "Arimo",Arial,sans-serif;margin:0 6px;color:#f6f2ea}
.card .go{position:absolute;right:10px;bottom:10px;width:18px;height:18px;border-radius:50%;border:1.5px solid var(--white);display:flex;align-items:center;justify-content:center}

/* why */
.why{top:1769px;left:0;width:1200px;height:448px}
.why-photo{position:absolute;inset:0;background:
  linear-gradient(180deg,rgba(48,82,138,.92) 0,rgba(52,86,140,.78) 40%,rgba(40,74,126,.88) 100%),
  linear-gradient(180deg,#6d8aa8 0,#5e7d5a 45%,#3d5d3e 100%)}
.why-eyebrow{color:var(--white)}
.why-eyebrow .line{background:var(--white)}
.why-item{position:absolute;top:1919px;width:230px;text-align:center;color:var(--white)}
.why-icon{width:140px;height:140px;margin:0 auto;border-radius:50%;border:3px solid var(--white);padding:6px;background:rgba(255,255,255,.25)}
.why-icon div{width:100%;height:100%;border-radius:50%;background:#f3f1ec;display:flex;align-items:center;justify-content:center}
.why-item h3{font:700 15px/17px "Arimo",Arial,sans-serif;margin-top:24px}
.why-item p{font:400 10px/14px "Arimo",Arial,sans-serif;margin-top:5px;padding:0 8px}

/* cta */
.cta-band{top:2882px;left:0;width:1200px;height:395px;background:
  linear-gradient(180deg,rgba(32,32,30,.94),rgba(34,36,32,.96)),linear-gradient(90deg,#3b4433,#2a2d27)}
.cta{top:2761px;left:145px;width:910px;height:233px;background:var(--sage);border-radius:3px}
.cta-title{position:absolute;left:0;width:1200px;top:2821px;text-align:center;color:var(--white);font:300 31px/38px "Roboto",Arial,sans-serif}

/* footer */
.foot-head{position:absolute;top:3054px;font:300 16.5px "Roboto",Arial,sans-serif;color:var(--white)}
.foot-text{position:absolute;font:400 9.5px/16px "Arimo",Arial,sans-serif;color:#e8e6e1}
.foot-divider{position:absolute;top:3054px;width:1px;height:160px;background:rgba(255,255,255,.18)}
.foot-links{position:absolute;left:394px;top:3090px;list-style:none;font:400 9.5px/20.3px "Arimo",Arial,sans-serif;color:#e8e6e1}
.foot-row{position:absolute;display:flex;align-items:center;gap:10px;font:400 9.5px/13px "Arimo",Arial,sans-serif;color:#e8e6e1}
.foot-row .ico{width:17px;height:17px;border-radius:50%;background:#dcd9d2;display:flex;align-items:center;justify-content:center;flex:none}
.field{position:absolute;left:923px;top:3095px;width:155px;height:32px;border:1px solid #d8d6d0;border-radius:16px;padding-left:14px;font:400 9.5px/30px "Arimo",Arial,sans-serif;color:#e8e6e1}
.copy{position:absolute;left:0;top:3240px;width:1200px;text-align:center;font:400 9px "Arimo",Arial,sans-serif;color:#e8e6e1}
</style>
</head>
<body>

<div class="stripe" style="top:0"><span></span><span></span><span></span><span></span></div>

<!-- hero -->
<header class="abs hero">
  <div class="hero-photo" role="img" aria-label="Young green seedling sprouting from a small earth globe resting on dark soil and pebbles"></div>
  <div class="logo" style="left:121px;top:30px"><span class="mark"></span>RTM Global</div>
  <nav class="nav">
    <a class="active" style="left:517px">Home</a>
    <a style="left:595px">About Us</a>
    <a style="left:680px">Services</a>
    <a style="left:789px">Why Choose RTM?</a>
    <a style="left:903px">Our Impact</a>
  </nav>
  <a class="btn btn-contact">Contact Us<span class="dot"><svg viewBox="0 0 14 14"><path d="M3 7h8M8 4l3 3-3 3" stroke="#8a9878" stroke-width="1.6" fill="none"/></svg></span></a>
  <div class="hero-rule"></div>
  <h1 class="hero-title">Revolutionizing<br>Agriculture With<br><b>Regenerative<br>Solutions</b></h1>
  <ul class="hero-list">
    <li>Mobile Drip Irrigation</li>
    <li>Regenerative Technologies</li>
    <li>Agronomy</li>
    <li>Soil Health</li>
  </ul>
  <a class="btn" style="left:122px;top:522px;width:136px;height:38px">Get Started<span class="dot"><svg viewBox="0 0 14 14"><path d="M3 7h8M8 4l3 3-3 3" stroke="#3f5f8e" stroke-width="1.6" fill="none"/></svg></span></a>
</header>

<!-- mission -->
<section>
  <div class="ghost-word" style="left:121px;top:813px;transform:rotate(90deg) translateY(-58px)">RTM Global</div>
  <div class="frame-back" style="left:188px;top:809px;width:268px;height:377px"></div>
  <div class="ring" style="left:229px;top:800px;width:390px;height:390px"></div>
  <div class="disc" role="img" aria-label="Farmer operating a tiller inside a polytunnel greenhouse" style="left:254px;top:825px;width:340px;height:340px;background:linear-gradient(160deg,#e7ecee 0,#c9d1cf 35%,#8c8170 65%,#5a4a3a 100%)"></div>
  <div class="eyebrow" style="left:738px;top:858px">RTM Global<span class="line"></span></div>
  <div class="eyebrow" style="left:738px;top:874px">(Rooted Tillage and Meadowcraft)</div>
  <h2 class="title" style="left:738px;top:893px">Our Mission</h2>
  <p class="para" style="left:738px;top:937px;width:342px">At RTM, we are committed to reshaping the future of farming through regenerative agriculture. Our solutions go beyond sustainability, actively restoring ecosystems and improving soil health while delivering superior yields. With water-efficient irrigation, innovative agronomy, and a deep focus on soil vitality, we empower farmers to grow more sustainably and profitably.</p>
  <a class="btn" style="left:739px;top:1060px;width:129px;height:39px">Read More<span class="dot"><svg viewBox="0 0 14 14"><path d="M3 7h8M8 4l3 3-3 3" stroke="#3f5f8e" stroke-width="1.6" fill="none"/></svg></span></a>
</section>

<!-- services -->
<section>
  <div class="eyebrow center" style="top:1253px"><span class="line"></span>Services We Offer<span class="line"></span></div>
  <h2 class="title" style="left:0;width:1200px;text-align:center;top:1268px">Our Core Products and Services</h2>

  <article class="card" style="left:121px">
    <div class="shot" role="img" aria-label="Young plants growing beside lab glassware and technology" style="background:linear-gradient(135deg,#6d7f58,#2f3a2a 60%,#8aa06a)"></div>
    <h3>Regenerative<br>Agricultural Technologies:</h3>
    <p>Unlock the future of farming with the latest practices and tools designed to rebuild ecosystems, improve biodiversity, and restore soil carbon levels.</p>
    <span class="go"><svg width="10" height="10" viewBox="0 0 10 10"><path d="M1 5h8M6 2l3 3-3 3" stroke="#fff" stroke-width="1.3" fill="none"/></svg></span>
  </article>
  <article class="card" style="left:365px">
    <div class="shot" role="img" aria-label="Hands holding a tablet above rows of drip irrigation lines" style="background:linear-gradient(160deg,#9aa596,#6e8a5c 50%,#a7846a)"></div>
    <h3>Mobile Drip Irrigation (MDI)</h3>
    <p>Our advanced irrigation system maximizes water use efficiency, reduces waste, and promotes healthier crops.</p>
    <span class="go"><svg width="10" height="10" viewBox="0 0 10 10"><path d="M1 5h8M6 2l3 3-3 3" stroke="#fff" stroke-width="1.3" fill="none"/></svg></span>
  </article>
  <article class="card" style="left:608px">
    <div class="shot" role="img" aria-label="Cupped hands holding soil with a small seedling" style="background:radial-gradient(circle at 50% 60%,#7a5540,#c6c2bb 70%)"></div>
    <h3>Agronomy Services</h3>
    <p>Expert advice and customized crop management plans to boost productivity while supporting regenerative outcomes.</p>
    <span class="go"><svg width="10" height="10" viewBox="0 0 10 10"><path d="M1 5h8M6 2l3 3-3 3" stroke="#fff" stroke-width="1.3" fill="none"/></svg></span>
  </article>
  <article class="card" style="left:853px">
    <div class="shot" role="img" aria-label="Seedling in dark soil with glowing technology graphics" style="background:radial-gradient(circle at 30% 45%,#6c8a3a,#2a2a28 55%,#4a4845)"></div>
    <h3>Soil Health Solutions</h3>
    <p>From analysis to rehabilitation, we help you restore soil fertility, improve water retention, and reduce dependency on chemical inputs.</p>
    <span class="go"><svg width="10" height="10" viewBox="0 0 10 10"><path d="M1 5h8M6 2l3 3-3 3" stroke="#fff" stroke-width="1.3" fill="none"/></svg></span>
  </article>

  <a class="btn" style="left:514px;top:1672px;width:172px;height:41px">View All Services<span class="dot"><svg viewBox="0 0 14 14"><path d="M3 7h8M8 4l3 3-3 3" stroke="#3f5f8e" stroke-width="1.6" fill="none"/></svg></span></a>
</section>

<!-- why choose -->
<section class="abs why">
  <div class="why-photo" role="img" aria-label="Irrigation sprinklers watering wide green crop fields under a blue tint"></div>
</section>
<div class="eyebrow center why-eyebrow" style="top:1827px;color:#fff"><span class="line"></span>Our Reason<span class="line"></span></div>
<h2 class="title" style="left:0;width:1200px;text-align:center;top:1843px;color:#fff;font-size:32px">Why Choose RTM?</h2>

<div class="why-item" style="left:119px">
  <div class="why-icon"><div><svg width="70" height="70" viewBox="0 0 70 70" fill="#7d8a6c"><path d="M33 14h4v32h-4z"/><path d="M35 20c-8 0-12-5-12-10 7 0 12 4 12 10zm0 0c8 0 12-5 12-10-7 0-12 4-12 10zM35 32c-8 0-12-5-12-10 7 0 12 4 12 10zm0 0c8 0 12-5 12-10-7 0-12 4-12 10z"/><path d="M14 44h42v5H14zM20 52h30l-4 6H24z"/></svg></div></div>
  <h3>Champions of<br>Regenerative Agriculture:</h3>
  <p>We don't just sustain—we regenerate, creating long-term benefits for the environment and your farm.</p>
</div>
<div class="why-item" style="left:362px">
  <div class="why-icon"><div><svg width="70" height="70" viewBox="0 0 70 70" fill="none" stroke="#7d8a6c" stroke-width="3"><path d="M35 14a14 14 0 0 0-8 25v6h16v-6a14 14 0 0 0-8-25z"/><path d="M29 50h12M31 55h8"/><path d="M35 21l2.5 5.5 6 .5-4.5 4 1.5 6-5.5-3.5-5.5 3.5 1.5-6-4.5-4 6-.5z" fill="#7d8a6c" stroke="none"/></svg></div></div>
  <h3>Cutting-Edge Innovation:</h3>
  <p>Access the latest technologies that promote ecosystem restoration and climate resilience.</p>
</div>
<div class="why-item" style="left:605px">
  <div class="why-icon"><div><svg width="70" height="70" viewBox="0 0 70 70" fill="#7d8a6c"><path d="M23 14h24v12a12 12 0 0 1-24 0z"/><path d="M23 17h-7v5a8 8 0 0 0 8 8M47 17h7v5a8 8 0 0 1-8 8" fill="none" stroke="#7d8a6c" stroke-width="3"/><path d="M32 38h6v8h-6zM25 46h20v6H25zM21 54h28v4H21z"/></svg></div></div>
  <h3>Tailored for Your Success:</h3>
  <p>We work with you to create strategies that meet the unique needs of your farm and community.</p>
</div>
<div class="why-item" style="left:852px">
  <div class="why-icon"><div><svg width="70" height="70" viewBox="0 0 70 70" fill="none" stroke="#7d8a6c" stroke-width="3"><path d="M15 35a20 20 0 0 1 34-14M55 35a20 20 0 0 1-34 14"/><path d="M49 13v8h-8M21 57v-8h8"/><circle cx="35" cy="35" r="9" fill="#7d8a6c" stroke="none"/></svg></div></div>
  <h3>Global Expertise:</h3>
  <p>Decades of experience bringing sustainable solutions to diverse farming environments worldwide.</p>
</div>

<!-- impact -->
<section>
  <div class="eyebrow" style="left:122px;top:2419px">Our Impact<span class="line"></span></div>
  <h2 class="title" style="left:122px;top:2435px">Our Impact</h2>
  <p class="para" style="left:122px;top:2480px;width:370px">We are proud to help farmers build resilient farms, sequester carbon, and regenerate the land. Our approach ensures healthy soils, vibrant ecosystems, and productive crops for generations to come.</p>
  <a class="btn" style="left:122px;top:2552px;width:130px;height:39px">Read More<span class="dot"><svg viewBox="0 0 14 14"><path d="M3 7h8M8 4l3 3-3 3" stroke="#3f5f8e" stroke-width="1.6" fill="none"/></svg></span></a>

  <div class="frame-back" style="left:743px;top:2341px;width:269px;height:354px"></div>
  <div class="ring" style="left:610px;top:2325px;width:390px;height:390px"></div>
  <div class="disc" role="img" aria-label="Two farmers with a tablet inspecting green crops in a field" style="left:635px;top:2350px;width:340px;height:340px;background:linear-gradient(180deg,#dfe6e8 0,#b9c6c0 30%,#6f9a4a 55%,#4c7a32 100%)"></div>
  <div class="ghost-word" style="left:1079px;top:2330px;transform:rotate(90deg)">RTM Global</div>
</section>

<!-- call to action -->
<div class="abs cta-band" role="img" aria-label="Dark farmland landscape"></div>
<div class="abs cta"></div>
<div class="eyebrow center" style="top:2801px;color:#fff"><span class="line" style="background:#fff"></span>Contact Us<span class="line" style="background:#fff"></span></div>
<h2 class="cta-title">Start your New journey with RTM Global<br>(Rooted Tillage and Meadowcraft)</h2>
<a class="btn" style="left:532px;top:2908px;width:135px;height:39px">Contact Us<span class="dot"><svg viewBox="0 0 14 14"><path d="M3 7h8M8 4l3 3-3 3" stroke="#3f5f8e" stroke-width="1.6" fill="none"/></svg></span></a>

<!-- footer -->
<footer>
  <div class="logo" style="left:121px;top:3062px"><span class="mark"></span>RTM Global</div>
  <p class="foot-text" style="left:121px;top:3116px;width:215px">At RTM, we are committed to reshaping the future of farming through regenerative agriculture. Our solutions go beyond sustainability, actively restoring ecosystems and improving soil health while delivering superior yields.</p>

  <div class="foot-divider" style="left:350px"></div>
  <div class="foot-divider" style="left:534px"></div>
  <div class="foot-divider" style="left:719px"></div>
  <div class="foot-divider" style="left:903px"></div>

  <h4 class="foot-head" style="left:393px">Quick Links</h4>
  <ul class="foot-links">
    <li>Home</li><li>About Us</li><li>Services</li><li>Why Choose RTM?</li><li>Our Impact</li><li>Contact Us</li>
  </ul>

  <h4 class="foot-head" style="left:554px">Contact Us</h4>
  <div class="foot-row" style="left:554px;top:3092px"><span class="ico"><svg width="9" height="11" viewBox="0 0 9 11"><path d="M4.5 0A4 4 0 0 0 .5 4c0 3 4 7 4 7s4-4 4-7a4 4 0 0 0-4-4zm0 5.5a1.5 1.5 0 1 1 0-3 1.5 1.5 0 0 1 0 3z" fill="#2a2824"/></svg></span>1480 Prairie Mill Road,<br>Suite 120, Austin, TX 78701</div>
  <div class="foot-row" style="left:554px;top:3133px"><span class="ico"><svg width="9" height="9" viewBox="0 0 9 9"><path d="M1.5 0.5l2 2-1 1.2a5 5 0 0 0 2.8 2.8l1.2-1 2 2-1.3 1.5C3.5 8.5.5 5.5.5 1.8z" fill="#2a2824"/></svg></span>555-014-2290</div>
  <div class="foot-row" style="left:554px;top:3167px"><span class="ico"><svg width="9" height="7" viewBox="0 0 9 7"><rect x=".5" y=".5" width="8" height="6" fill="none" stroke="#2a2824"/><path d="M.5.5l4 3.5 4-3.5" fill="none" stroke="#2a2824"/></svg></span>hello@rtmglobal.com</div>

  <h4 class="foot-head" style="left:770px">Follow Us</h4>
  <div class="foot-row" style="left:772px;top:3095px"><span class="ico"></span>Fieldbook</div>
  <div class="foot-row" style="left:772px;top:3120px"><span class="ico"></span>Snapgram</div>
  <div class="foot-row" style="left:772px;top:3146px"><span class="ico"></span>Chirper</div>
  <div class="foot-row" style="left:772px;top:3171px"><span class="ico"></span>Linkwork</div>

  <h4 class="foot-head" style="left:923px">Subscribe Newsletter</h4>
  <div class="field">Enter Your Email</div>
  <a class="btn" style="left:923px;top:3144px;width:128px;height:37px">Subscribe<span class="dot"><svg viewBox="0 0 14 14"><path d="M3 7h8M8 4l3 3-3 3" stroke="#3f5f8e" stroke-width="1.6" fill="none"/></svg></span></a>

  <p class="copy">© 2024 All Rights Reserved By RTM Global (Rooted Tillage and Meadowcraft)</p>
</footer>

<div class="stripe" style="top:3273px"><span></span><span></span><span></span><span></span></div>
</body>
</html>
```